Business Card Design Project

We require a professional business card designed for our consulting organisation that has the same theme and colours as our logo except for the grey.

Colours on the front should predominately be white however some reference to our logo colours except for the grey.

The back of the card should be have background colour that aligns with our logo colour.

Layout, style and design is up to the designer. So send through your designs

Details are attached in the word document project brief.

Target Market(s)

Target market are large corporate organisations

Industry/Entity Type

Business

Requirements
Must have
• Content on the front must have:

Dean Halvorsen
Managing Director

P: 0417 285 394
E: Dean@brevolinkpartners.com
W: www.brevolinkpartners.com

Content on the back must have the words:
Alliances
Placement
Training
Support

Design Colours
Must align to our logo

```html
<!DOCTYPE html>
<html lang="en">
<head>
<meta charset="utf-8">
<title>BrevoLink Partners – Business Card</title>
<link rel="stylesheet" href="https://fonts.googleapis.com/css2?family=Source+Sans+3:wght@400;600;700&display=swap">
<style>
  :root {
    --page-bg: #ffffff;
    --frame-line: #6b6b6b;
    --card-bg: #ffffff;
    --card-line: #2b2b2b;
    --brand-blue: #1b75c4;
    --divider: #8a8a8a;
    --ink: #231f20;
    --ink-reverse: #ffffff;
    --divider-reverse: rgba(255, 255, 255, 0.7);
  }
  html, body {
    margin: 0;
    padding: 0;
    width: 1200px;
    height: 901px;
    overflow: hidden;
    background: var(--page-bg);
    font-family: "Source Sans 3", "Myriad Pro", Arial, sans-serif;
    color: var(--ink);
  }
  .canvas {
    position: relative;
    width: 1200px;
    height: 901px;
    box-sizing: border-box;
    border: 1.5px solid var(--frame-line);
  }
  .card {
    position: absolute;
    left: 341px;
    width: 517px;
    height: 329px;
    box-sizing: border-box;
    background: var(--card-bg);
    border: 1.5px solid var(--card-line);
    border-radius: 9px;
  }
  .card--front { top: 115px; }
  .card--back  {
    top: 455px;
    background: var(--brand-blue);
    color: var(--ink-reverse);
  }

  .brand {
    position: absolute;
    display: flex;
    align-items: center;
    gap: 21px;
  }
  .card--front .brand { left: 28px; top: 31px; }
  .card--back  .brand { left: 17px; top: 24px; }

  .brand__mark {
    width: 46px;
    height: 46px;
    background: var(--brand-blue);
    border-radius: 4px;
  }
  .brand__name {
    color: var(--brand-blue);
    font-weight: 700;
    font-size: 23px;
    line-height: 23px;
  }
  .card--back .brand__mark { background: var(--ink-reverse); }
  .card--back .brand__name { color: var(--ink-reverse); }

  .details {
    position: absolute;
    border-left: 1.5px solid var(--divider);
    padding-left: 7px;
    font-size: 11.5px;
    line-height: 15.5px;
  }
  .card--front .details { left: 303px; top: 34px; height: 75px; }
  .card--back  .details {
    left: 300px;
    top: 18px;
    height: 64px;
    border-left-color: var(--divider-reverse);
  }

  .details__name { font-weight: 700; }
  .details__role { font-weight: 600; }
  .details p { margin: 0; }

  .card__web {
    position: absolute;
    bottom: 8px;
    font-size: 11px;
    font-weight: 700;
    transform: translateX(-50%);
    white-space: nowrap;
  }
  .card--front .card__web { left: 251px; }
  .card--back  .card__web { left: 222px; }
</style>
</head>
<body>
<main class="canvas">
  <section class="card card--front" aria-label="Card front">
    <div class="brand">
      <div class="brand__mark"></div>
      <div class="brand__name">BrevoLink<br>Partners</div>
    </div>
    <div class="details">
      <p class="details__name">Dean Halvorsen</p>
      <p class="details__role">Managing Director</p>
      <p>P: 0417 285 394</p>
      <p>E: Dean@brevolinkpartners.com</p>
      <p>W: www.brevolinkpartners.com</p>
    </div>
    <div class="card__web">www.brevolinkpartners.com</div>
  </section>

  <section class="card card--back" aria-label="Card back">
    <div class="brand">
      <div class="brand__mark"></div>
      <div class="brand__name">BrevoLink<br>Partners</div>
    </div>
    <div class="details">
      <p>Alliances</p>
      <p>Placement</p>
      <p>Training</p>
      <p>Support</p>
    </div>
    <div class="card__web">www.brevolinkpartners.com</div>
  </section>
</main>
</body>
</html>
```